PELTON RIDGE HEATING AND COOLING

Industry/Entity Type

Hvac

Requirements
Must have
• logo
My name: Doug Ferriblen
Phone number 555-304-9461
Text:
Furnace and AC repairs
New furnace and AC installation
Ductwork
Gas lines
Water Tanks
Tankless water heaters
Nice to have
• Profesional modern look

```html
<!DOCTYPE html>
<html lang="en">
<head>
<meta charset="utf-8">
<title>Pelton Ridge Heating and Cooling – Business Card</title>
<link href="https://fonts.googleapis.com/css2?family=Cinzel:wght@500;600&family=Montserrat:wght@400;500&display=swap" rel="stylesheet">
<style>
  :root{
    --backdrop:#1d1d20;
    --card-green:#6abf3a;
    --brand-blue:#1657a6;
    --paper:#ffffff;
    --ink-grey:#3a3a3a;
  }
  *{box-sizing:border-box;margin:0;padding:0}
  html,body{width:1200px;height:786px;overflow:hidden;background:var(--backdrop)}
  .stage{position:relative;width:1200px;height:786px}
  .card{
    position:absolute;top:228px;width:530px;height:330px;
    border:11px solid var(--card-green);
  }
  .card--front{left:45px;background:var(--paper)}
  .card--back{left:625px;background:var(--brand-blue)}

  .wordmark{font-family:"Cinzel",serif;font-weight:600;letter-spacing:1px;line-height:1.15}
  .card--front .wordmark{
    position:absolute;left:34px;top:118px;width:210px;
    color:var(--brand-blue);font-size:25px;text-align:center;
  }
  .wordmark .tagline{display:block;font-size:25px}
  .divider{position:absolute;left:268px;top:92px;width:1px;height:126px;background:var(--card-green)}
  .contact{position:absolute;left:292px;top:96px;font-family:"Montserrat",sans-serif;color:var(--ink-grey)}
  .contact .name{font-family:"Cinzel",serif;font-weight:500;font-size:19px;color:var(--brand-blue);letter-spacing:.5px}
  .contact .role{font-size:13px;margin:2px 0 12px}
  .contact ul{list-style:none}
  .contact li{display:flex;align-items:center;gap:7px;font-size:12.5px;margin-bottom:5px}
  .contact svg{width:11px;height:11px;fill:var(--brand-blue);flex:none}

  .card--back .wordmark{
    position:absolute;left:0;right:0;top:70px;text-align:center;
    color:var(--paper);font-size:34px;
  }
  .card--back .wordmark .tagline{font-size:34px}
  .rule{display:block;width:300px;height:1px;background:var(--paper);margin:10px auto 0}
  .services{
    position:absolute;left:0;right:0;bottom:38px;text-align:center;
    font-family:"Montserrat",sans-serif;color:var(--paper);font-size:13.5px;line-height:1.7;
  }
</style>
</head>
<body>
<main class="stage">
  <section class="card card--front" aria-label="Card front">
    <div class="wordmark">PELTON RIDGE<span class="tagline">HEATING AND COOLING</span></div>
    <div class="divider"></div>
    <div class="contact">
      <p class="name">DOUG FERRIBLEN</p>
      <p class="role">Director</p>
      <ul>
        <li><svg viewBox="0 0 24 24"><path d="M6.6 10.8a15 15 0 0 0 6.6 6.6l2.2-2.2a1 1 0 0 1 1-.25 11.4 11.4 0 0 0 3.6.57 1 1 0 0 1 1 1V20a1 1 0 0 1-1 1A17 17 0 0 1 3 4a1 1 0 0 1 1-1h3.5a1 1 0 0 1 1 1c0 1.25.2 2.45.57 3.57a1 1 0 0 1-.25 1z"/></svg>555-304-9461</li>
        <li><svg viewBox="0 0 24 24"><path d="M2 5h20v14H2zm2 2v.5l8 5 8-5V7zm0 2.9V17h16V9.9l-8 5z"/></svg>info@peltonridgehvac.com</li>
        <li><svg viewBox="0 0 24 24"><circle cx="12" cy="12" r="10"/></svg>www.peltonridgehvac.com</li>
      </ul>
    </div>
  </section>

  <section class="card card--back" aria-label="Card back">
    <div class="wordmark">PELTON RIDGE<span class="tagline">HEATING AND COOLING</span><span class="rule"></span></div>
    <p class="services">Furnace and AC repairs | New furnace and AC installation<br>Ductwork | Gas lines | Water Tanks | Tankless water heaters</p>
  </section>
</main>
</body>
</html>
```